Taskvora Software Business Card Design

We are a new organization called Taskvora. We are a software as a service provider. We deliver a project and program management solution via the internet, so everyone has the ability to work together and collaborate. Its an enterprise platform and we will focus on 50 plus employee company.

We have a website in place
www.taskvora-example.com

Use this as a start of producing the business card. The logo is there as well, but if you have a great and better solution...

Color scheme's could be inline with the website, but don't pin point on it. We can always change the website, logo, color scheme etc.

Target Market(s)

B2B, Projectmembers, projectmanagers, ICT, CTO, Marketing Managers

Industry/Entity Type

Software

Requirements
Must have
• Maarten Velsepol

Tel: +31 555 17 40 92
Mob: +31 6 902 36 517
maarten@taskvora-example.com
Keltenlaan 384b
9071 XK Oostervelde

Www.taskvora-example.com
social media links

```html
<!DOCTYPE html>
<html lang="en">
<head>
<meta charset="utf-8">
<title>Taskvora Business Card</title>
<link rel="stylesheet" href="https://fonts.googleapis.com/css2?family=Exo+2:wght@300;400;600;700&display=swap">
<style>
  :root {
    --stage: #d4d4d4;
    --paper: #f4f4f4;
    --lime: #a9bb2a;
    --sky: #1b9ae6;
    --tangerine: #ef800e;
    --white: #ffffff;
    --ink-soft: #e9efc8;
  }
  * { box-sizing: border-box; margin: 0; padding: 0; }
  html, body { width: 1200px; height: 861px; overflow: hidden; }
  body {
    background: var(--stage);
    font-family: "Exo 2", Arial, sans-serif;
    position: relative;
  }
  .card {
    position: absolute;
    top: 276px;
    width: 540px;
    height: 309px;
    background: var(--paper);
    overflow: hidden;
    box-shadow: 0 6px 18px rgba(0,0,0,0.18);
  }
  .card--front { left: 40px; }
  .card--back { left: 620px; }

  /* front side */
  .front-band {
    position: absolute; left: 0; top: 0; width: 100%; height: 140px;
    background: var(--lime);
  }
  .front-pointer { position: absolute; left: 250px; top: 139px; }
  .wordmark {
    position: absolute;
    font-weight: 300;
    letter-spacing: 1px;
    line-height: 1;
    white-space: nowrap;
  }
  .front-band .wordmark {
    left: 0; width: 100%; top: 30px; text-align: center;
    font-size: 64px; color: var(--white);
  }
  .front-url {
    position: absolute; left: 0; width: 100%; top: 104px; text-align: center;
    color: var(--white); font-size: 14px; letter-spacing: 5px; font-weight: 400;
  }
  .role {
    position: absolute; width: 96px; height: 96px; border-radius: 50%;
    border: 3px solid var(--white);
    box-shadow: 0 1px 4px rgba(0,0,0,0.2);
    display: flex; align-items: center; justify-content: center;
    text-align: center; color: var(--white);
    font-size: 10px; letter-spacing: 0.5px; line-height: 1.3; text-transform: uppercase;
  }
  .role--team { left: 110px; top: 196px; background: var(--sky); }
  .role--pm { left: 222px; top: 172px; background: var(--tangerine); }
  .role--mgmt { left: 334px; top: 148px; background: var(--lime); }

  /* back side */
  .back-band {
    position: absolute; left: 0; top: 150px; width: 100%; height: 159px;
    background: var(--lime);
  }
  .back-pointer { position: absolute; left: 440px; top: 131px; }
  .card--back .wordmark {
    left: 110px; top: 58px; font-size: 66px; color: var(--lime);
  }
  .holder {
    position: absolute; right: 26px; top: 170px; text-align: right; color: var(--white);
  }
  .holder__name { font-size: 22px; font-weight: 700; letter-spacing: 0.5px; white-space: nowrap; }
  .holder__position { font-size: 15px; font-weight: 300; color: var(--ink-soft); }
  .contacts {
    position: absolute; left: 22px; top: 176px; list-style: none;
    color: var(--white); font-size: 11.5px; line-height: 17px;
  }
  .contacts li { display: flex; align-items: center; gap: 6px; white-space: nowrap; }
  .contacts svg { width: 12px; height: 12px; flex: none; }
</style>
</head>
<body>
  <section class="card card--front" aria-label="Card front">
    <div class="front-band">
      <span class="wordmark">Taskvora</span>
      <span class="front-url">www.taskvora-example.com</span>
    </div>
    <svg class="front-pointer" width="40" height="20" viewBox="0 0 40 20"><polygon points="0,0 40,0 20,20" fill="var(--lime)"/></svg>
    <div class="role role--team">Team<br>member</div>
    <div class="role role--pm">Project<br>manager</div>
    <div class="role role--mgmt">Management</div>
  </section>

  <section class="card card--back" aria-label="Card back">
    <span class="wordmark">Taskvora</span>
    <svg class="back-pointer" width="40" height="20" viewBox="0 0 40 20"><polygon points="0,20 40,20 20,0" fill="var(--lime)"/></svg>
    <div class="back-band"></div>
    <div class="holder">
      <p class="holder__name">MAARTEN VELSEPOL</p>
      <p class="holder__position">Position</p>
    </div>
    <ul class="contacts">
      <li><svg viewBox="0 0 12 12"><circle cx="6" cy="6" r="6" fill="#fff"/><path d="M6 2.5a2.3 2.3 0 0 0-2.3 2.3C3.7 6.6 6 9.5 6 9.5s2.3-2.9 2.3-4.7A2.3 2.3 0 0 0 6 2.5z" fill="var(--lime)"/></svg>Keltenlaan 384b 9071 XK Oostervelde</li>
      <li><svg viewBox="0 0 12 12"><circle cx="6" cy="6" r="6" fill="#fff"/><path d="M3.5 3c.5-.5 1-.4 1.3.1l.6 1c.2.4 0 .7-.3 1 .4.8 1 1.4 1.8 1.8.3-.3.6-.5 1-.3l1 .6c.5.3.6.8.1 1.3-.8.8-2 .6-3.6-1S2.7 3.8 3.5 3z" fill="var(--lime)"/></svg>+31 555 17 40 92</li>
      <li><svg viewBox="0 0 12 12"><circle cx="6" cy="6" r="6" fill="#fff"/><rect x="4" y="2.5" width="4" height="7" rx="0.8" fill="var(--lime)"/></svg>+31 6 902 36 517</li>
      <li><svg viewBox="0 0 12 12"><circle cx="6" cy="6" r="6" fill="#fff"/><rect x="2.8" y="3.8" width="6.4" height="4.4" fill="var(--lime)"/><path d="M2.8 3.8 6 6.3l3.2-2.5" stroke="#fff" stroke-width="0.7" fill="none"/></svg>maarten@taskvora-example.com</li>
      <li><svg viewBox="0 0 12 12"><circle cx="6" cy="6" r="6" fill="#fff"/><circle cx="6" cy="6" r="3.2" fill="none" stroke="var(--lime)" stroke-width="0.9"/><path d="M2.8 6h6.4M6 2.8v6.4" stroke="var(--lime)" stroke-width="0.8"/></svg>www.taskvora-example.com</li>
      <li><svg viewBox="0 0 12 12"><circle cx="6" cy="6" r="6" fill="#fff"/></svg>TaskvoraCOM</li>
      <li><svg viewBox="0 0 12 12"><circle cx="6" cy="6" r="6" fill="#fff"/></svg>Taskvora</li>
    </ul>
  </section>
</body>
</html>
```